Brantley Yard Services Flyer Design

I need a new flyer design for my business, Brantley Yard Services. I’ll be providing my old flyer and logo as references. The new flyer should feature updated wording, contact information, logos, and photos, but still keep the original “What We Do” section and include the phrase “Don’t See? Just Ask!” somewhere near the services. The flyer needs to look great in black and white for door-to-door handouts but also be eye-catching and professional enough for social media use.

The updated content should include the headline “Transforming Outdoor Spaces with Hard Work & Precision” and highlight three main service areas: Landscaping Services (project-based landscaping to clean, prepare, and transform outdoor spaces with precision), Property Cleanup (quick hauls, debris removal, or full cleanouts—no job too big or small), and Ground Preparation (pad preparation, brush removal, and fire lines—making properties safe, functional, and project-ready).

Please also include a “Why Choose Us?” section that lists: Locally owned since 2022, Reliable & affordable – no corners cut, Professional results you can trust, LICENSED AND Insured, and Quality work / on time / references / flexible / follow-up.

At the bottom, include the contact details: Call or Text Today!
www.brantleyyard.example
| sales@brantleyyard.example
| (555) 014-2793

The overall design should be clean, professional, and easy to read with a layout that clearly shows what we offer. Use visuals that represent outdoor services, landscaping, and property cleanup/prep work. I want something that feels trustworthy, family-friendly, and modern.
Use the same photo of leaf clean up from the original flyer if possible.
Our company colors are also black and white. For the most part.

```html
<!DOCTYPE html>
<html lang="en">
<head>
<meta charset="UTF-8">
<title>Brantley Yard Services Flyer</title>
<link href="https://fonts.googleapis.com/css2?family=Anton&family=Lexend:wght@400;500&family=Montserrat:wght@600;700;800&display=swap" rel="stylesheet">
<style>
  :root {
    --ink: #000000;
    --paper: #ffffff;
    --wash: #f4f4f1;
    --burlap: #b59870;
    --sky: #b8c6d6;
    --muted: #333333;
  }
  * { margin: 0; padding: 0; box-sizing: border-box; }
  html, body { width: 927px; height: 1200px; overflow: hidden; }
  body {
    background: var(--paper);
    font-family: 'Lexend', sans-serif;
    color: var(--ink);
  }
  .flyer {
    position: relative;
    width: 927px;
    height: 1200px;
    overflow: hidden;
    background: radial-gradient(ellipse at 70% 60%, #ecece8 0%, var(--wash) 45%, #fafaf8 100%);
  }
  .brand {
    position: absolute;
    left: 36px; top: 50px;
    display: flex; align-items: center; gap: 16px;
  }
  .brand-mark { width: 78px; height: 78px; background: var(--ink); }
  .brand-name {
    font-family: 'Montserrat', sans-serif;
    font-weight: 800;
    font-size: 38px;
    line-height: 1.02;
    text-transform: uppercase;
  }
  .hero-photo {
    position: absolute;
    left: 0; top: 188px;
    width: 567px; height: 322px;
    border-radius: 0 260px 300px 0 / 0 160px 200px 0;
    background: linear-gradient(90deg, rgba(122,154,46,0.95) 0%, rgba(110,130,40,0.9) 40%, var(--burlap) 62%, #a98c64 100%);
  }
  .headline-panel {
    position: absolute;
    left: 496px; top: 34px;
    width: 441px; height: 338px;
    border-radius: 170px 0 0 170px;
    background: var(--paper);
  }
  .headline-panel-inner {
    position: absolute;
    left: 506px; top: 45px;
    width: 421px; height: 317px;
    border-radius: 160px 0 0 160px;
    background: var(--ink);
  }
  .headline {
    position: absolute;
    right: 39px; top: 96px;
    font-family: 'Anton', sans-serif;
    font-style: italic;
    font-weight: 400;
    font-size: 49px;
    line-height: 50px;
    text-align: right;
    text-transform: uppercase;
    color: var(--paper);
    letter-spacing: -0.5px;
  }
  .pill {
    position: absolute;
    background: var(--ink);
    color: var(--paper);
    font-family: 'Montserrat', sans-serif;
    font-weight: 800;
    text-transform: uppercase;
  }
  .pill-why {
    left: 605px; top: 374px;
    width: 322px; height: 54px;
    border-radius: 27px 0 0 27px;
    font-size: 26px;
    padding-left: 40px;
    line-height: 54px;
  }
  .why-list {
    position: absolute;
    left: 622px; top: 436px;
    width: 298px;
    list-style: none;
    font-size: 15px;
    line-height: 20px;
  }
  .why-list li {
    position: relative;
    padding-left: 18px;
    margin-bottom: 2px;
  }
  .why-list li::before {
    content: "";
    position: absolute;
    left: 3px; top: 8px;
    width: 5px; height: 5px;
    border-radius: 50%;
    background: var(--ink);
  }
  .pill-what {
    left: 0; top: 539px;
    width: 352px; height: 55px;
    border-radius: 0 28px 28px 0;
    font-size: 27px;
    padding-left: 41px;
    line-height: 55px;
  }
  .licensed {
    position: absolute;
    left: 420px; top: 536px;
    width: 162px; height: 58px;
    border-radius: 0 29px 29px 0;
    background: var(--ink);
    color: var(--paper);
    font-family: 'Montserrat', sans-serif;
    font-weight: 700;
    font-size: 21px;
    line-height: 24px;
    padding: 5px 0 0 22px;
    text-transform: uppercase;
  }
  .shield {
    position: absolute;
    left: 361px; top: 525px;
    width: 72px; height: 84px;
  }
  .service-col { position: absolute; top: 632px; }
  .service-col h2 {
    font-family: 'Montserrat', sans-serif;
    font-weight: 800;
    font-size: 27px;
    text-transform: uppercase;
    margin-bottom: 16px;
  }
  .service-col ul { list-style: none; font-size: 18px; }
  .service-col li { display: flex; align-items: center; height: 30.7px; }
  .service-col li svg { width: 19px; height: 19px; margin-right: 13px; flex: none; }
  .col-remove { left: 36px; }
  .col-install { left: 328px; }
  .col-maint { left: 516px; }
  .ask-line { position: absolute; top: 836px; height: 2px; background: var(--ink); }
  .ask-line.left { left: 45px; width: 235px; }
  .ask-line.right { left: 652px; width: 235px; }
  .ask {
    position: absolute; left: 328px; top: 820px;
    font-family: 'Montserrat', sans-serif;
    font-weight: 800;
    font-size: 25px;
  }
  .footer-band {
    position: absolute; left: 0; top: 1007px;
    width: 927px; height: 193px;
    background: var(--ink);
  }
  .card {
    position: absolute; top: 872px; height: 215px;
    background: var(--ink);
    border-radius: 14px;
    overflow: hidden;
  }
  .card-photo {
    position: absolute; left: 9px; right: 9px; top: 9px; height: 136px;
    border-radius: 8px 8px 0 0;
  }
  .card-label {
    position: absolute; left: 0; right: 0; bottom: 0; height: 70px;
    background: var(--paper);
    border-radius: 0 0 14px 14px;
    text-align: center;
    padding: 7px 12px 0;
  }
  .card-title {
    font-family: 'Montserrat', sans-serif;
    font-weight: 800;
    font-size: 16px;
    line-height: 20px;
    text-transform: uppercase;
  }
  .card-text {
    font-size: 10px;
    line-height: 13px;
    color: var(--muted);
    margin-top: 2px;
  }
  .card-landscape { left: 48px; width: 252px; }
  .card-landscape .card-photo { background: linear-gradient(180deg, #8fa0ad 0%, #6f7a5a 40%, #a89a86 70%, #b7aa95 100%); }
  .card-cleanup { left: 341px; width: 249px; }
  .card-cleanup .card-photo { background: linear-gradient(180deg, #7c6a4a 0%, #5a4a3a 40%, #8a8574 70%, #a7aa92 100%); }
  .card-prep { left: 632px; width: 253px; }
  .card-prep .card-photo { background: linear-gradient(180deg, var(--sky) 0%, #9aa0a8 40%, #8d877c 65%, #b6a891 100%); }
  .call {
    position: absolute; left: 0; width: 927px; top: 1104px;
    text-align: center;
    color: var(--paper);
    font-family: 'Montserrat', sans-serif;
    font-weight: 700;
    font-size: 24px;
  }
  .contact {
    position: absolute; top: 1150px;
    display: flex; align-items: center; gap: 10px;
    color: var(--paper);
    font-family: 'Montserrat', sans-serif;
    font-weight: 700;
    font-size: 17px;
  }
  .contact svg { width: 22px; height: 22px; flex: none; }
  .contact-web { left: 47px; }
  .contact-phone { left: 357px; }
  .contact-mail { left: 605px; }
</style>
</head>
<body>
<div class="flyer">

  <div class="brand">
    <div class="brand-mark"></div>
    <div class="brand-name">Brantley Yard<br>Services</div>
  </div>

  <div class="hero-photo" role="img" aria-label="Photo of a rake gathering autumn leaves on green grass beside a burlap leaf bag"></div>

  <div class="headline-panel"></div>
  <div class="headline-panel-inner"></div>
  <h1 class="headline">Transforming<br>Outdoor Spaces<br>With Hard Work &amp;<br>Precision</h1>

  <div class="pill pill-why">Why Choose Us?</div>
  <ul class="why-list">
    <li>Locally owned since 2022</li>
    <li>Reliable &amp; affordable – no corners cut</li>
    <li>Professional results you can trust</li>
    <li>Licensed and Insured</li>
    <li>Quality work</li>
    <li>On Time</li>
    <li>References</li>
    <li>Flexible</li>
    <li>Follow-up</li>
  </ul>

  <div class="pill pill-what">What We Do</div>
  <div class="licensed">Licensed<br>&amp; Insured</div>
  <svg class="shield" viewBox="0 0 72 84" aria-hidden="true">
    <path d="M36 2 L70 12 L70 42 C70 62 54 76 36 82 C18 76 2 62 2 42 L2 12 Z" fill="var(--paper)"/>
    <path d="M36 6 L66 15 L66 42 C66 60 52 72 36 78 C20 72 6 60 6 42 L6 15 Z" fill="var(--ink)"/>
    <path d="M20 42 L32 54 L54 26" fill="none" stroke="var(--paper)" stroke-width="6" stroke-linecap="round" stroke-linejoin="round"/>
  </svg>

  <div class="service-col col-remove">
    <h2>Remove</h2>
    <ul>
      <li><svg viewBox="0 0 20 20"><circle cx="10" cy="10" r="10" fill="var(--ink)"/><path d="M5.5 10.2 L8.7 13.3 L14.5 7" fill="none" stroke="var(--paper)" stroke-width="2.4" stroke-linecap="round" stroke-linejoin="round"/></svg>Junk Removal</li>
      <li><svg viewBox="0 0 20 20"><circle cx="10" cy="10" r="10" fill="var(--ink)"/><path d="M5.5 10.2 L8.7 13.3 L14.5 7" fill="none" stroke="var(--paper)" stroke-width="2.4" stroke-linecap="round" stroke-linejoin="round"/></svg>Trash &amp; Waste hauling</li>
      <li><svg viewBox="0 0 20 20"><circle cx="10" cy="10" r="10" fill="var(--ink)"/><path d="M5.5 10.2 L8.7 13.3 L14.5 7" fill="none" stroke="var(--paper)" stroke-width="2.4" stroke-linecap="round" stroke-linejoin="round"/></svg>Yard &amp; Garden cleanup</li>
      <li><svg viewBox="0 0 20 20"><circle cx="10" cy="10" r="10" fill="var(--ink)"/><path d="M5.5 10.2 L8.7 13.3 L14.5 7" fill="none" stroke="var(--paper)" stroke-width="2.4" stroke-linecap="round" stroke-linejoin="round"/></svg>Appliance Removal</li>
    </ul>
  </div>

  <div class="service-col col-install">
    <h2>Install</h2>
    <ul>
      <li><svg viewBox="0 0 20 20"><circle cx="10" cy="10" r="10" fill="var(--ink)"/><path d="M5.5 10.2 L8.7 13.3 L14.5 7" fill="none" stroke="var(--paper)" stroke-width="2.4" stroke-linecap="round" stroke-linejoin="round"/></svg>Mulch</li>
      <li><svg viewBox="0 0 20 20"><circle cx="10" cy="10" r="10" fill="var(--ink)"/><path d="M5.5 10.2 L8.7 13.3 L14.5 7" fill="none" stroke="var(--paper)" stroke-width="2.4" stroke-linecap="round" stroke-linejoin="round"/></svg>D.G.</li>
      <li><svg viewBox="0 0 20 20"><circle cx="10" cy="10" r="10" fill="var(--ink)"/><path d="M5.5 10.2 L8.7 13.3 L14.5 7" fill="none" stroke="var(--paper)" stroke-width="2.4" stroke-linecap="round" stroke-linejoin="round"/></svg>Plants</li>
      <li><svg viewBox="0 0 20 20"><circle cx="10" cy="10" r="10" fill="var(--ink)"/><path d="M5.5 10.2 L8.7 13.3 L14.5 7" fill="none" stroke="var(--paper)" stroke-width="2.4" stroke-linecap="round" stroke-linejoin="round"/></svg>Rock</li>
    </ul>
  </div>

  <div class="service-col col-maint">
    <h2>Maintenance &amp; Other</h2>
    <ul>
      <li><svg viewBox="0 0 20 20"><circle cx="10" cy="10" r="10" fill="var(--ink)"/><path d="M5.5 10.2 L8.7 13.3 L14.5 7" fill="none" stroke="var(--paper)" stroke-width="2.4" stroke-linecap="round" stroke-linejoin="round"/></svg>Yard Cleanup</li>
      <li><svg viewBox="0 0 20 20"><circle cx="10" cy="10" r="10" fill="var(--ink)"/><path d="M5.5 10.2 L8.7 13.3 L14.5 7" fill="none" stroke="var(--paper)" stroke-width="2.4" stroke-linecap="round" stroke-linejoin="round"/></svg>Weed prevention (pre-emergent)</li>
      <li><svg viewBox="0 0 20 20"><circle cx="10" cy="10" r="10" fill="var(--ink)"/><path d="M5.5 10.2 L8.7 13.3 L14.5 7" fill="none" stroke="var(--paper)" stroke-width="2.4" stroke-linecap="round" stroke-linejoin="round"/></svg>Roof &amp; Gutter cleaning</li>
      <li><svg viewBox="0 0 20 20"><circle cx="10" cy="10" r="10" fill="var(--ink)"/><path d="M5.5 10.2 L8.7 13.3 L14.5 7" fill="none" stroke="var(--paper)" stroke-width="2.4" stroke-linecap="round" stroke-linejoin="round"/></svg>Fence &amp; deck staining</li>
    </ul>
  </div>

  <div class="ask-line left"></div>
  <div class="ask">Don’t See? Just Ask!</div>
  <div class="ask-line right"></div>

  <div class="footer-band"></div>

  <div class="card card-landscape">
    <div class="card-photo" role="img" aria-label="Photo of a finished backyard with a gravel patio, stone retaining wall and wooden fence"></div>
    <div class="card-label">
      <div class="card-title">Landscaping</div>
      <p class="card-text">Project-based landscaping to clean, prepare, and transform outdoor spaces with precision.</p>
    </div>
  </div>
  <div class="card card-cleanup">
    <div class="card-photo" role="img" aria-label="Photo of a hauled pile of junk, old furniture and debris from a property cleanout"></div>
    <div class="card-label">
      <div class="card-title">Property Cleanup</div>
      <p class="card-text">Quick hauls, debris removal, or full cleanouts — no job too big or small.</p>
    </div>
  </div>
  <div class="card card-prep">
    <div class="card-photo" role="img" aria-label="Photo of a graded ground pad with stacked pavers, a compact excavator and a work truck"></div>
    <div class="card-label">
      <div class="card-title">Ground Preparation</div>
      <p class="card-text">Pad preparation, brush removal, and fire lines — making properties safe, functional, and project-ready.</p>
    </div>
  </div>

  <div class="call">Call or Text Today!</div>

  <div class="contact contact-web">
    <svg viewBox="0 0 24 24" aria-hidden="true"><circle cx="12" cy="12" r="11" fill="var(--paper)"/><g fill="none" stroke="var(--ink)" stroke-width="1.3"><circle cx="12" cy="12" r="7"/><ellipse cx="12" cy="12" rx="3" ry="7"/><path d="M5 12 H19 M6 8.5 H18 M6 15.5 H18"/></g></svg>
    <span>www.brantleyyard.example</span>
  </div>
  <div class="contact contact-phone">
    <svg viewBox="0 0 24 24" aria-hidden="true"><circle cx="12" cy="12" r="11" fill="var(--paper)"/><path d="M8.2 6.5 L10 6.3 L11 9.2 L9.8 10.3 C10.5 11.9 11.9 13.4 13.6 14.2 L14.8 13 L17.6 14.1 L17.4 15.9 C15.8 17.6 11.6 16 9.6 13.8 C7.6 11.7 6.5 8.2 8.2 6.5 Z" fill="var(--ink)"/></svg>
    <span>(555) 014-2793</span>
  </div>
  <div class="contact contact-mail">
    <svg viewBox="0 0 24 24" aria-hidden="true"><circle cx="12" cy="12" r="11" fill="var(--paper)"/><rect x="6" y="8" width="12" height="8.5" rx="1" fill="none" stroke="var(--ink)" stroke-width="1.4"/><path d="M6.3 8.5 L12 13 L17.7 8.5" fill="none" stroke="var(--ink)" stroke-width="1.4"/></svg>
    <span>sales@brantleyyard.example</span>
  </div>

</div>
</body>
</html>
```